Ridgeline Outfitters Business Cards

Recently had a logo done with Artfolio and now looking for a business card to go along with it.

Target Market(s)

Ridgeline Outfitters is a weapons dealer. My market will be primarily men, hunting, shooting type.

Industry/Entity Type

Business

Contact Information for Business Card

I selected double sided, but this is not required, single or double is going to be fine. I picture the logo on one side, or perhaps just the circle which contains "RO" with the remaining info on the other side.

Font styles to use
Sans Serif

Requirements
Must have
• My name: Milo Brandt
• Title: Owner
• tel: 612-555-0187
• web: www.ridgelineoutfittersmn.example
Nice to have
• I like the concept of a black business card. I would like to keep the colors monotone, black, grey, white or red. Red is acceptable because it is in the logo. I have also seen cards that are matte black with shiny black as well, perhaps for the logo (or circle RO) part of the logo.
• I will upload a couple of the logos for use, and also an example I just found of the black on black. and some others that have a nice contrast.
Should not have
• lots of colors are not wanted.

```html
<!DOCTYPE html>
<html lang="en">
<head>
<meta charset="utf-8">
<title>Ridgeline Outfitters Business Cards</title>
<link href="https://fonts.googleapis.com/css2?family=Roboto:wght@400;700&display=swap" rel="stylesheet">
<style>
  :root {
    --backdrop: #3b322d;
    --card: #17191c;
    --card-edge: #101113;
    --silver: #c9cbce;
    --silver-dark: #8c8f93;
    --red: #e3262f;
    --text-light: #dcdde0;
    --text-muted: #a9abae;
  }
  * { box-sizing: border-box; margin: 0; padding: 0; }
  html, body {
    width: 1200px; height: 769px; overflow: hidden;
    background: var(--backdrop);
    font-family: "Roboto", Arial, sans-serif;
  }
  .canvas {
    position: relative; width: 1200px; height: 769px;
    display: flex; align-items: center; justify-content: center; gap: 60px;
  }
  .card {
    position: relative; width: 520px; height: 297px;
    background: var(--card);
    border: 1px solid var(--card-edge);
    box-shadow: 0 18px 40px rgba(0,0,0,.45);
  }
  /* front: contact side */
  .card-front .mark-placeholder {
    position: absolute; top: 34px; right: 40px;
    width: 84px; height: 84px; border-radius: 50%;
    background: linear-gradient(135deg, var(--silver), var(--silver-dark));
  }
  .contact-block { position: absolute; left: 38px; bottom: 30px; }
  .person-name {
    color: var(--red); font-weight: 700; font-size: 20px;
    text-transform: uppercase; letter-spacing: .3px;
  }
  .person-title { color: var(--text-muted); font-size: 14px; margin-top: 2px; margin-bottom: 12px; }
  .contact-list { list-style: none; }
  .contact-item {
    display: flex; align-items: center; gap: 10px;
    color: var(--text-light); font-size: 14px; line-height: 22px;
  }
  .contact-item svg { width: 13px; height: 13px; flex: none; fill: var(--red); }
  /* back: brand side */
  .card-back { display: flex; align-items: center; justify-content: center; gap: 16px; }
  .brand-dot {
    width: 58px; height: 58px; border-radius: 50%;
    border: 4px solid var(--silver);
  }
  .brand-name {
    color: var(--silver); font-weight: 700; font-size: 26px;
    text-transform: uppercase; letter-spacing: 1px;
  }
</style>
</head>
<body>
<main class="canvas">
  <section class="card card-front">
    <div class="mark-placeholder" role="img" aria-label="Brand mark area"></div>
    <div class="contact-block">
      <h1 class="person-name">Milo Brandt</h1>
      <p class="person-title">Owner</p>
      <ul class="contact-list">
        <li class="contact-item">
          <svg viewBox="0 0 16 16"><path d="M3.5 1l3 3-1.6 2c1 2 2.6 3.6 4.6 4.6l2-1.6 3 3-2 2.5C6.5 14 2 9.5 1 3.5z"/></svg>
          612-555-0187
        </li>
        <li class="contact-item">
          <svg viewBox="0 0 16 16"><path d="M1 3h14v10H1z M1.8 3.6L8 8.6l6.2-5V4.8L8 9.8 1.8 4.8z" fill-rule="evenodd"/></svg>
          info@ridgelineoutfittersmn.example
        </li>
        <li class="contact-item">
          <svg viewBox="0 0 16 16"><circle cx="8" cy="8" r="7"/><path d="M1 8h14M8 1c-3 3.5-3 10.5 0 14M8 1c3 3.5 3 10.5 0 14" stroke="#17191c" stroke-width="1.2" fill="none"/></svg>
          www.ridgelineoutfittersmn.example
        </li>
      </ul>
    </div>
  </section>
  <section class="card card-back">
    <span class="brand-dot"></span>
    <span class="brand-name">Ridgeline Outfitters</span>
  </section>
</main>
</body>
</html>
```